依頼詳細
ご覧いただきまして、有難うございます!

制作イメージなどの詳細を記載しております依頼書、及び、画像素材を以下URLからダウンロードしてご確認頂けますと幸いです。
(依頼書、画像素材の格納フォルダ)
https://www.filemoribox.example/sh/qp4rt8wkmxz3vy7/BBtr2hmzp_kLoWxYQ8nRtEvPa?dl=0

継続的にLPの改修を予定しておりまして、継続的にページのデザイン制作をしていただける方を探しております。長期的な関係を築ければと思います。

上記URL先に格納しております依頼書をお読み頂き、ご質問等ありましたら、気軽にお問い合わせください。
たくさんのご応募をお待ちしております!
記載項目
依頼書、画像素材は以下格納フォルダからご確認をお願いします。
(依頼書、画像素材の格納フォルダ)
サイズ
• 横1000px x 縦1600px
希望イメージ
シンプル 複雑
単色 カラフル
暗い 明るい
日常 高級
遊び心 厳粛
未来的 伝統的
女性的 男性的
希望する色
指定はありませんが、既存LPに合わないものは避けて下さい。
納品ファイル
• 高解像度JPG (.jpg)
• イラストレーター形式 (.ai)
• フォトショップ形式 (.psd)
補足説明
■ 選んだ理由

読み手に伝えたい内容が、最も伝わると思ったデザインでしたので、選ばせて頂きました。

■ 提案者全員のお礼・コメント

皆様、とても素敵な提案を頂きまして誠に有難う御座いました。
素敵で気になるデザインがたくさんあり、とても選定に悩みました。
今回、ご縁がなかった方々とも、今後ご一緒させて頂ければと思います。
重ねて、ご提案頂きましたこと、御礼申し上げます。

```html
<!DOCTYPE html>
<html lang="ja">
<head>
<meta charset="utf-8">
<title>VELORA カスタマイズサプリ</title>
<link href="https://fonts.googleapis.com/css2?family=Noto+Sans+JP:wght@500;700;900&display=swap" rel="stylesheet">
<style>
  :root{
    --ink:#2b2b33;
    --pink:#e8307a;
    --pink-soft:#f9d3e3;
    --gold:#c9a76a;
    --sun:#f5c842;
    --moon:#b9bcc6;
    --bg:#ffffff;
    --panel-gap:#ffffff;
  }
  *{margin:0;padding:0;box-sizing:border-box}
  html,body{width:750px;height:1200px;overflow:hidden;background:var(--bg)}
  body{font-family:"Noto Sans JP",sans-serif;color:var(--ink)}
  .banner{position:relative;width:750px;height:1200px;overflow:hidden;background:var(--bg)}
  .brand{position:absolute;left:26px;top:22px;font-size:22px;font-weight:700;letter-spacing:5px;color:var(--ink)}
  .headline{position:absolute;left:0;top:62px;width:750px;text-align:center;line-height:1}
  .headline .lead{display:block;font-size:44px;font-weight:700;letter-spacing:1px}
  .headline .lead small{font-size:38px;font-weight:500}
  .headline .main{display:block;margin-top:22px;font-size:62px;font-weight:900;letter-spacing:2px}
  .headline .accent{color:var(--pink);font-size:86px;background:linear-gradient(transparent 70%,var(--pink-soft) 70%)}
  .scenes{position:absolute;left:0;top:240px;width:750px;height:410px}
  .badge{position:absolute;width:62px;height:62px;border-radius:50%;display:flex;align-items:center;justify-content:center;font-size:24px;font-weight:700;color:#fff}
  .badge.morning{left:64px;top:120px;background:var(--sun);box-shadow:0 0 0 7px rgba(245,200,66,.35)}
  .badge.noon{left:392px;top:130px;background:var(--sun);box-shadow:0 0 0 7px rgba(245,200,66,.35)}
  .badge.night{left:640px;top:136px;background:var(--moon);box-shadow:0 0 0 7px rgba(185,188,198,.35)}
  .caption{position:absolute;background:rgba(255,255,255,.92);padding:12px 14px;text-align:center;font-weight:700;font-size:24px;line-height:1.35}
  .caption em{font-style:normal;color:var(--pink);font-size:30px}
  .caption.morning{left:26px;top:225px;width:190px}
  .caption.noon{left:290px;top:215px;width:190px}
  .caption.night{left:548px;top:225px;width:180px}
  .supervised{position:absolute;left:262px;top:728px;width:226px;height:46px;border-radius:23px;background:var(--gold);color:#fff;font-size:26px;font-weight:700;display:flex;align-items:center;justify-content:center;letter-spacing:3px}
  .pitch{position:absolute;left:0;top:790px;width:750px;text-align:center;line-height:1}
  .pitch .tag{display:inline-block;font-size:38px;font-weight:700;color:var(--pink);padding-bottom:8px;border-bottom:3px solid var(--pink)}
  .pitch .name{display:block;margin-top:18px;font-size:50px;font-weight:900;letter-spacing:2px}
  .packs{position:absolute;left:0;top:930px;width:750px;height:270px}
</style>
</head>
<body>
<div class="banner">
  <div class="brand">VELORA</div>

  <h1 class="headline">
    <span class="lead"><small>3つのサプリで</small>仕事と休息に</span>
    <span class="main"><span class="accent">本気</span>で向き合う!</span>
  </h1>

  <div class="scenes">
    <svg width="750" height="410" viewBox="0 0 750 410">
      <defs>
        <linearGradient id="gMorning" x1="0" y1="0" x2="0" y2="1"><stop offset="0" stop-color="#e9e2d9"/><stop offset="1" stop-color="#c9a58b"/></linearGradient>
        <linearGradient id="gNoon" x1="0" y1="0" x2="0" y2="1"><stop offset="0" stop-color="#dfe3e6"/><stop offset="1" stop-color="#5b6470"/></linearGradient>
        <linearGradient id="gNight" x1="0" y1="0" x2="0" y2="1"><stop offset="0" stop-color="#eef0f1"/><stop offset="1" stop-color="#c4b3a6"/></linearGradient>
      </defs>
      <g role="img" aria-label="朝、笑顔の女性の写真"><polygon points="0,0 272,0 252,410 0,410" fill="url(#gMorning)"/></g>
      <g role="img" aria-label="昼、電話をするスーツ姿の男性の写真"><polygon points="284,0 514,0 494,410 264,410" fill="url(#gNoon)"/></g>
      <g role="img" aria-label="夜、くつろいで笑う女性の写真"><polygon points="526,0 750,0 750,410 506,410" fill="url(#gNight)"/></g>
    </svg>
    <div class="badge morning">朝</div>
    <div class="badge noon">昼</div>
    <div class="badge night">夜</div>
    <p class="caption morning">1日に必要な<br><em>栄養20種</em></p>
    <p class="caption noon">エナジーで<br><em>シャキッ</em>と<br>元気に</p>
    <p class="caption night">CBDで<br><em>ぐっすり</em><br>リラックス</p>
  </div>

  <div class="supervised">医師監修</div>

  <div class="pitch">
    <span class="tag">あなた専用に組合せを変更できる</span>
    <span class="name">カスタマイズサプリ</span>
  </div>

  <div class="packs">
    <svg width="750" height="270" viewBox="0 0 750 270">
      <defs>
        <linearGradient id="gPack" x1="0" y1="0" x2="1" y2="1"><stop offset="0" stop-color="#fafafa"/><stop offset="1" stop-color="#dcdde0"/></linearGradient>
        <linearGradient id="gPackPink" x1="0" y1="0" x2="1" y2="1"><stop offset="0" stop-color="#f6eef4"/><stop offset="1" stop-color="#e3c9dc"/></linearGradient>
        <linearGradient id="gPackBlue" x1="0" y1="0" x2="1" y2="1"><stop offset="0" stop-color="#eef3f7"/><stop offset="1" stop-color="#c9d6e2"/></linearGradient>
      </defs>
      <g role="img" aria-label="マルチビタミン&ミネラルのパウチ2袋">
        <rect x="110" y="10" width="135" height="225" rx="6" fill="url(#gPackBlue)"/>
        <rect x="28" y="30" width="150" height="235" rx="6" fill="url(#gPack)"/>
      </g>
      <g role="img" aria-label="エナジーのパウチ2袋">
        <rect x="355" y="10" width="135" height="225" rx="6" fill="url(#gPackPink)"/>
        <rect x="272" y="30" width="150" height="235" rx="6" fill="url(#gPack)"/>
      </g>
      <g role="img" aria-label="リラックスCBDのパウチ2袋">
        <rect x="600" y="10" width="135" height="225" rx="6" fill="url(#gPackBlue)"/>
        <rect x="516" y="30" width="150" height="235" rx="6" fill="url(#gPack)"/>
      </g>
    </svg>
  </div>
</div>
</body>
</html>
```